Lomi Vardell
Incorporated
Lomi Vardell -
Creative Brief
Use specific fonts
Please use font that would fulfill the requirements of the comment description below
Professional
Derek Holm
Operations Manager
Town of Wrenfield, NV
lomivardell@quillmesh.net
Our company extracts essential and fragrance oil from flowers. We blend our own brand-name perfume and fragrances. Please design cards to reflect a corporate appeal, with feminine luxury, higher end sophistication, yet gentle and soft. Attached is chosen logo. Feel free to take the abstract symbol and name out of the background if deemed necessary.

```html
<!DOCTYPE html>
<html lang="en">
<head>
<meta charset="utf-8">
<title>Lomi Vardell – Business Card Set</title>
<link href="https://fonts.googleapis.com/css2?family=EB+Garamond:wght@400;600&display=swap" rel="stylesheet">
<style>
  :root {
    --page: #ffffff;
    --label: #6f6f6f;
    --ink-black: #0d0d0d;
    --gold: #c9a14a;
    --gold-light: #e9cf86;
    --gold-deep: #8a6a2a;
    --bronze: #7a5b33;
    --bronze-dark: #5f4525;
    --name-yellow: #f1d23c;
    --text-muted: #b88a4a;
  }
  * { margin: 0; padding: 0; box-sizing: border-box; }
  html, body {
    width: 1200px; height: 927px; overflow: hidden;
    background: var(--page);
    font-family: "EB Garamond", Georgia, serif;
  }
  .sheet { position: relative; width: 1200px; height: 927px; }
  .side-label {
    position: absolute; left: 350px; top: 98px;
    font-size: 36px; letter-spacing: 1px; color: var(--label);
  }
  .card {
    position: absolute; width: 485px; height: 280px; overflow: hidden;
    box-shadow: 0 18px 22px -14px rgba(0,0,0,0.45);
  }
  .card--front { left: 105px; top: 150px; background: var(--ink-black); }
  .card--back-black { left: 610px; top: 150px;
    background: radial-gradient(ellipse at 50% 45%, #3a3a3a 0%, #161616 70%, #0a0a0a 100%); }
  .card--pattern { left: 105px; top: 512px; }
  .card--bronze { left: 610px; top: 512px;
    background: linear-gradient(180deg, var(--bronze) 0%, var(--bronze-dark) 100%); }

  .front-curve { position: absolute; inset: 0; }
  .brand-block {
    position: absolute; left: 22px; top: 52px; width: 220px;
    display: flex; flex-direction: column; align-items: center; gap: 10px;
  }
  .brand-dot {
    width: 32px; height: 32px; border-radius: 50%;
    background: linear-gradient(135deg, var(--gold-light), var(--gold-deep));
  }
  .brand-name {
    font-size: 15px; font-weight: 400; letter-spacing: 3.5px;
    text-transform: uppercase; color: var(--gold); white-space: nowrap;
  }
  .contact { position: absolute; left: 307px; top: 96px; color: var(--text-muted); }
  .contact__name { font-size: 21px; font-weight: 600; color: var(--name-yellow); line-height: 1.1; }
  .contact__role { font-size: 11px; margin-top: 2px; }
  .contact__city { font-size: 11px; margin-top: 36px; }
  .contact__lines { margin-top: 18px; font-size: 11px; line-height: 1.6; }
  .contact__lines b { color: #ffffff; font-weight: 600; margin-right: 3px; }

  .back-mark {
    position: absolute; inset: 0;
    display: flex; flex-direction: column; align-items: center; justify-content: center; gap: 10px;
  }
  .back-mark .brand-dot { width: 40px; height: 40px; }
  .back-mark .brand-name { font-size: 13px; letter-spacing: 4px; }

  .pattern-fill {
    position: absolute; inset: 0;
    background: radial-gradient(ellipse at 50% 40%, #2c2c2c 0%, #151515 75%, #0b0b0b 100%);
  }
</style>
</head>
<body>
<main class="sheet">
  <div class="side-label">FRONT</div>

  <section class="card card--front" aria-label="Business card front">
    <svg class="front-curve" viewBox="0 0 485 280" width="485" height="280" aria-hidden="true">
      <defs>
        <linearGradient id="goldBand" x1="0" y1="1" x2="1" y2="0">
          <stop offset="0" stop-color="#8a6a2a"/>
          <stop offset="0.5" stop-color="#e9cf86"/>
          <stop offset="1" stop-color="#b88a3a"/>
        </linearGradient>
      </defs>
      <path d="M0 0 H300 C262 80 224 210 60 280 H0 Z" fill="url(#goldBand)"/>
      <path d="M0 0 H288 C246 72 206 204 0 266 Z" fill="#ffffff"/>
    </svg>
    <div class="brand-block">
      <span class="brand-dot"></span>
      <span class="brand-name">Lomi Vardell</span>
    </div>
    <div class="contact">
      <div class="contact__name">Derek Holm</div>
      <div class="contact__role">Operations Manager</div>
      <div class="contact__city">Town of Wrenfield, NV</div>
      <div class="contact__lines">
        <div><b>P:</b>(555) 555-0147</div>
        <div><b>E:</b>lomivardell@quillmesh.net</div>
      </div>
    </div>
  </section>

  <section class="card card--back-black" aria-label="Business card back, black">
    <div class="back-mark">
      <span class="brand-dot"></span>
      <span class="brand-name">Lomi Vardell</span>
    </div>
  </section>

  <section class="card card--pattern" aria-label="Business card back, patterned">
    <div class="pattern-fill" role="img" aria-label="Dark charcoal card with a faint repeating floral brand pattern"></div>
  </section>

  <section class="card card--bronze" aria-label="Business card back, bronze">
    <div class="back-mark">
      <span class="brand-dot"></span>
      <span class="brand-name">Lomi Vardell</span>
    </div>
  </section>
</main>
</body>
</html>
```